Creative Web Site to Sell Geology Classes for Homeschooling

I am starting a business to sell a variety of geology classes for homeschoolers. I am targeting classes for kids with dyslexia, although others will benefit as well. The classes will be delivered by mail. Each class will have a video, a manual, and rock samples. I need a landing page that I can link over to seven other pages, a page with a template for products, and a template of the pages that will not have products. All should be easy to edit. All pages should display well with handheld devices (phones), as well as desktops.

Designs look the same

```html
<!DOCTYPE html>
<html lang="en">
<head>
<meta charset="utf-8">
<title>Stone Trail Academy — Geology Classes for Homeschoolers</title>
<link href="https://fonts.googleapis.com/css2?family=Questrial&family=Lato:wght@400;700&display=swap" rel="stylesheet">
<style>
:root{
  --coral:#f7766b;
  --coral-deep:#f26a5f;
  --purple:#65587b;
  --purple-dark:#564a6b;
  --teal:#5fcfae;
  --teal-soft:#7fd9c0;
  --yellow:#fde28f;
  --ink:#4f4463;
  --grey:#7d7787;
  --white:#ffffff;
  --hero-grey:#d9d7de;
  --footer-bar:#6b5c80;
}
*{box-sizing:border-box;margin:0;padding:0}
html,body{width:1200px;height:3523px;overflow:hidden}
body{position:relative;background:var(--white);font-family:"Lato",sans-serif;color:var(--ink)}
.abs{position:absolute}
.heading{font-family:"Questrial",sans-serif;text-transform:uppercase;letter-spacing:1px}

/* header */
.site-header{position:absolute;left:0;top:0;width:1200px;height:95px;background:var(--white)}
.brand{position:absolute;left:140px;top:14px;display:flex;align-items:center;gap:12px}
.brand-dot{width:66px;height:66px;border-radius:50%;background:var(--coral)}
.brand-name{font-family:"Questrial",sans-serif;font-size:22px;line-height:22px;color:var(--coral);text-transform:uppercase;width:140px}
.topbar{position:absolute;right:140px;top:16px;display:flex;gap:30px;font-size:13px;color:var(--purple)}
.topbar span{display:flex;align-items:center;gap:10px}
.topbar i{display:inline-block;width:26px;height:26px;border-radius:50%;background:var(--coral)}
.topbar svg{display:block}
.main-nav{position:absolute;right:140px;top:66px;display:flex;gap:44px;font-family:"Questrial",sans-serif;font-size:12.5px;text-transform:uppercase;color:var(--purple)}
.main-nav .active{color:var(--coral)}

/* hero */
.hero{position:absolute;left:0;top:95px;width:1200px;height:530px;background:linear-gradient(90deg,#dcdae0 0%,#d6d3da 38%,#c9b8a6 55%,#a9948a 72%,#6a7a8e 88%,#3e4d63 100%)}
.hero-title{position:absolute;left:140px;top:288px;width:430px;font-size:24px;line-height:32px;color:var(--coral)}
.btn{position:absolute;display:flex;align-items:center;justify-content:space-between;height:36px;padding:0 6px 0 20px;border-radius:18px;font-family:"Questrial",sans-serif;font-size:13px;text-transform:uppercase;letter-spacing:.5px}
.btn b{width:26px;height:26px;border-radius:50%;display:flex;align-items:center;justify-content:center}
.btn-solid{background:var(--purple);color:var(--white)}
.btn-solid b{background:var(--white)}
.btn-outline{background:var(--white);border:2px solid currentColor}
.btn-outline b{background:currentColor}

/* section titles */
.section-title{position:absolute;left:0;width:1200px;text-align:center;font-size:28px;color:var(--coral)}
.divider{position:absolute;left:455px;width:290px;height:24px}

/* chapters */
.chapter-img{position:absolute;width:216px;height:216px;border-radius:42%;border:4px solid;padding:6px;background:var(--white)}
.chapter-img div{width:100%;height:100%;border-radius:40%}
.chapter-title{position:absolute;width:300px;text-align:center;font-family:"Questrial",sans-serif;font-size:17px;line-height:23px}
.chapter-text{position:absolute;width:300px;text-align:center;font-size:12.5px;line-height:18px;color:var(--ink)}

/* about */
.about{position:absolute;left:0;top:1320px;width:1200px;height:493px;background:var(--yellow)}
.about-photo{position:absolute;left:142px;top:80px;width:360px;height:320px;border-radius:60px;border:6px solid var(--coral);background:linear-gradient(135deg,#f3e2cf,#d9b79c 50%,#9fb7c8)}
.about-photo-small{position:absolute;left:380px;top:250px;width:180px;height:170px;border-radius:50px;border:6px solid var(--coral);background:linear-gradient(135deg,#eef1f4,#c9d3dc 60%,#a7b4c0)}
.about-title{position:absolute;left:600px;top:82px;font-size:25px;color:var(--coral)}
.about-lead{position:absolute;left:600px;top:160px;width:455px;font-size:13px;line-height:20px;font-weight:700;color:var(--purple)}
.about-body{position:absolute;left:600px;top:218px;width:455px;font-size:12px;line-height:20.5px;color:var(--purple)}

/* learn */
.learn{position:absolute;left:0;top:1813px;width:1200px;height:520px;background:var(--coral)}
.learn-item{position:absolute;width:320px;text-align:center;color:var(--white);font-size:13.5px;line-height:22px}
.learn-item svg{display:block;margin:0 auto 30px}

/* blog */
.post-img{position:absolute;top:2558px;width:291px;height:212px}
.post-date{position:absolute;left:0;top:0;width:44px;height:54px;background:var(--teal);color:var(--white);font-family:"Questrial",sans-serif;font-size:13px;text-align:center;line-height:18px;padding-top:8px}
.post-title{position:absolute;top:2790px;width:291px;font-size:13px;line-height:19px;font-weight:700;color:var(--purple)}
.post-text{position:absolute;top:2842px;width:291px;font-size:12px;line-height:19px;color:var(--ink)}

/* footer */
.site-footer{position:absolute;left:0;top:3036px;width:1200px;height:447px;background:linear-gradient(120deg,#7fd6c0,#5ccfae 45%,#78d6bd)}
.footer-title{position:absolute;font-size:24px;color:var(--white)}
.field{position:absolute;height:36px;background:rgba(255,255,255,.35);border:1px solid rgba(255,255,255,.6);font-size:11px;color:var(--white);padding:10px 10px}
.contact-row{position:absolute;left:766px;display:flex;gap:16px;color:var(--white)}
.contact-row i{flex:none;width:30px;height:30px;border-radius:50%;background:var(--purple);display:flex;align-items:center;justify-content:center}
.contact-row strong{display:block;font-size:11px;text-transform:uppercase;letter-spacing:.5px}
.contact-row p{font-size:12px;line-height:17px}
.follow{position:absolute;left:788px;top:336px;display:flex;align-items:center;gap:10px;color:var(--white)}
.follow .heading{font-size:16px;margin-right:14px}
.follow i{width:28px;height:28px;border-radius:50%;background:var(--purple)}
.copyright{position:absolute;left:0;top:3483px;width:1200px;height:40px;background:var(--footer-bar);color:var(--white);font-size:12px;text-align:center;line-height:40px}
</style>
</head>
<body>

<header class="site-header">
  <div class="brand"><span class="brand-dot"></span><span class="brand-name">Stone Trail Academy</span></div>
  <div class="topbar">
    <span><i></i>info@stonetrailacademy.com</span>
    <span><i></i>123-456-7890</span>
  </div>
  <nav class="main-nav">
    <span class="active">Home</span><span>About Us</span><span>Online Programs &#8964;</span><span>Reviews</span><span>News</span><span>Contact Us</span>
  </nav>
</header>

<section class="hero" role="img" aria-label="Photo of two children examining a rock with a magnifying glass">
  <h1 class="hero-title heading">We provide geology classes for homeschooling specially to kids with dyslexia</h1>
  <a class="btn btn-solid" style="left:140px;top:402px;width:164px">Learn More <b><svg width="10" height="10" viewBox="0 0 10 10"><path d="M2 0l7 5-7 5z" fill="#65587b"/></svg></b></a>
</section>

<h2 class="section-title heading" style="top:720px">Physical Geology Which Includes Chapters On</h2>
<svg class="divider" style="top:776px" viewBox="0 0 290 24"><line x1="0" y1="14" x2="120" y2="14" stroke="#65587b"/><line x1="170" y1="14" x2="290" y2="14" stroke="#65587b"/><circle cx="145" cy="12" r="11" fill="none" stroke="#65587b" stroke-width="1.5"/><path d="M136 16l6-7 4 4 3-3 5 6z" fill="#65587b"/></svg>

<div class="chapter-img" style="left:162px;top:820px;border-color:var(--purple)"><div role="img" aria-label="Photo of blue and white mineral specimen" style="background:radial-gradient(circle,#9fd8d6,#4fa3a8 55%,#c4c8c4)"></div></div>
<div class="chapter-img" style="left:492px;top:820px;border-color:var(--coral)"><div role="img" aria-label="Photo of folded layered rock" style="background:linear-gradient(120deg,#c99462,#8a5a36 50%,#d8b48a)"></div></div>
<div class="chapter-img" style="left:822px;top:820px;border-color:var(--teal)"><div role="img" aria-label="Image of planet Earth" style="background:radial-gradient(circle at 40% 40%,#7fb3e0,#2c5fa2 60%,#0e1d3b)"></div></div>

<h3 class="chapter-title" style="left:120px;top:1078px;color:var(--purple)">Mineral Types, Properties<br>And Uses</h3>
<h3 class="chapter-title" style="left:450px;top:1078px;color:var(--coral)">Rock Deformation and<br>Mountain Building</h3>
<h3 class="chapter-title" style="left:780px;top:1078px;color:var(--teal)">Earth's Spheres and<br>Internal Structure</h3>
<p class="chapter-text" style="left:120px;top:1138px">Lorem ipsum dolor sit amet, consectetuer adipiscing elit, sed diam nonummy nibh euism tincidunt exerci tation</p>
<p class="chapter-text" style="left:450px;top:1138px">Lorem ipsum dolor sit amet, consectetuer adipiscing elit, sed diam nonummy nibh euism tincidunt exerci tation</p>
<p class="chapter-text" style="left:780px;top:1138px">Lorem ipsum dolor sit amet, consectetuer adipiscing elit, sed diam nonummy nibh euism tincidunt exerci tation</p>
<a class="btn btn-solid" style="left:205px;top:1208px;width:135px;height:32px;font-size:11.5px">Learn More <b style="width:22px;height:22px"><svg width="9" height="9" viewBox="0 0 10 10"><path d="M2 0l7 5-7 5z" fill="#65587b"/></svg></b></a>
<a class="btn btn-outline" style="left:533px;top:1208px;width:135px;height:32px;font-size:11.5px;color:var(--coral)">Learn More <b style="width:20px;height:20px"><svg width="8" height="8" viewBox="0 0 10 10"><path d="M2 0l7 5-7 5z" fill="#fff"/></svg></b></a>
<a class="btn btn-outline" style="left:863px;top:1208px;width:135px;height:32px;font-size:11.5px;color:var(--teal)">Learn More <b style="width:20px;height:20px"><svg width="8" height="8" viewBox="0 0 10 10"><path d="M2 0l7 5-7 5z" fill="#fff"/></svg></b></a>

<section class="about">
  <div class="about-photo" role="img" aria-label="Photo of two girls smiling at a laptop"></div>
  <div class="about-photo-small" role="img" aria-label="Photo of a boy at a desk raising his hand"></div>
  <h2 class="about-title heading">About Stone Trail Academy</h2>
  <svg class="abs" style="left:600px;top:126px" width="150" height="24" viewBox="0 0 150 24"><circle cx="12" cy="12" r="11" fill="none" stroke="#65587b" stroke-width="1.5"/><path d="M3 16l6-7 4 4 3-3 5 6z" fill="#65587b"/><line x1="30" y1="14" x2="150" y2="14" stroke="#65587b"/></svg>
  <p class="about-lead">Lorem ipsum dolor sit amet, consectetuer adipiscing elit, sed diam nummy nibh euismod tincidunt ut laoreet dolore magna aliquam erat volutpat.</p>
  <p class="about-body">Lorem ipsum dolor sit amet, consectetuer adipiscing elit, sed diam nonummy nibh euismod tincidunt ut laoreet dolore magna aliquam erat volutpat. Ut wisi enim ad minim veniam, quis nostrud exerci tation ullamcorper suscipit lobortis nisl ut aliquip ex ea commodo consequat. Duis autem vel eum iriure dolor in hendrerit in vulputate velit esse molestie consequat, vel illum dolore eu feugiat nulla facilisis at vero eros et accumsan et iusto odio dignissim qui blandit praesent luptatum zzril delenit augue duis dolore te feugait nulla facilisi.</p>
  <a class="btn btn-solid" style="left:600px;top:390px;width:135px;height:34px;font-size:12px">Learn More <b style="width:24px;height:24px"><svg width="9" height="9" viewBox="0 0 10 10"><path d="M2 0l7 5-7 5z" fill="#65587b"/></svg></b></a>
</section>

<section class="learn">
  <h2 class="section-title heading" style="top:112px;color:var(--yellow);font-size:27px">What You'll Learn</h2>
  <svg class="divider" style="top:150px" viewBox="0 0 290 24"><line x1="20" y1="12" x2="125" y2="12" stroke="#fff" stroke-opacity=".6"/><line x1="165" y1="12" x2="270" y2="12" stroke="#fff" stroke-opacity=".6"/><circle cx="145" cy="12" r="8" fill="none" stroke="#fde28f" stroke-width="1.5"/></svg>
  <div class="learn-item" style="left:90px;top:222px">
    <svg width="84" height="84" viewBox="0 0 84 84" fill="none" stroke="#fff" stroke-width="2.5"><circle cx="42" cy="42" r="36"/><path d="M6 42h72M42 6c-14 14-14 58 0 72M42 6c14 14 14 58 0 72M14 22c16 8 40 8 56 0M14 62c16-8 40-8 56 0"/></svg>
    Learn how geology influences<br>everything from the shape of the<br>landscape to natural events
  </div>
  <div class="learn-item" style="left:440px;top:210px">
    <svg width="84" height="96" viewBox="0 0 84 96" fill="none" stroke="#fff" stroke-width="2.5"><circle cx="42" cy="30" r="20"/><path d="M30 22l8 6-4 8M50 16l-4 10 8 6"/><path d="M8 30v28c0 10 10 16 20 22v14M76 30v28c0 10-10 16-20 22v14M18 50l12 14M66 50l-12 14"/></svg>
    Learn about the history and workings of<br>planet Earth
  </div>
  <div class="learn-item" style="left:790px;top:222px">
    <svg width="90" height="84" viewBox="0 0 90 84" fill="none" stroke="#fff" stroke-width="2.5" stroke-linejoin="round"><path d="M6 34L26 8l34 2 24 30-10 36-40 4L8 60z"/><path d="M26 8l10 30 24-28M36 38l48 2M36 38l-2 42M36 38L6 34"/></svg>
    Learn about global phenomena, rocks,<br>crystals,plate tectonics, geologic time,<br>and how rocks form.
  </div>
  <svg class="abs" style="left:0;top:400px" width="1200" height="120" viewBox="0 0 1200 120" preserveAspectRatio="none"><path d="M0 80 Q300 10 600 60 Q900 10 1200 80 V120 H0z" fill="#fff"/><path d="M0 62 Q300 -6 600 42 Q900 -6 1200 62" fill="none" stroke="#fff" stroke-width="4"/></svg>
</section>

<h2 class="section-title heading" style="top:2450px">Latest Blog Posts</h2>
<svg class="divider" style="top:2496px" viewBox="0 0 290 24"><line x1="0" y1="14" x2="120" y2="14" stroke="#65587b"/><line x1="170" y1="14" x2="290" y2="14" stroke="#65587b"/><circle cx="145" cy="12" r="11" fill="none" stroke="#65587b" stroke-width="1.5"/><path d="M136 16l6-7 4 4 3-3 5 6z" fill="#65587b"/></svg>

<div class="post-img" style="left:143px;background:linear-gradient(135deg,#8a8c7a,#5d6a72 50%,#a79c86)" role="img" aria-label="Photo of students on a field trip at a rock face"><span class="post-date">FEB<br>07</span></div>
<div class="post-img" style="left:455px;background:linear-gradient(135deg,#b8ad9c,#8f8576 50%,#c9c1b3)" role="img" aria-label="Photo of a geologist in a hard hat examining rock"><span class="post-date">FEB<br>07</span></div>
<div class="post-img" style="left:768px;background:linear-gradient(120deg,#cfe0ea,#9fb6c8 45%,#7b4fa0 75%,#4e2b70)" role="img" aria-label="Photo of quartz and amethyst crystals"><span class="post-date">FEB<br>07</span></div>

<h3 class="post-title" style="left:143px">Lorem ipsum dolor sit amet, consectetuer adipiscing elit, sed diam nonummy</h3>
<h3 class="post-title" style="left:455px">Lorem ipsum dolor sit amet, consectetuer adipiscing elit, sed diam nonummy</h3>
<h3 class="post-title" style="left:768px">Lorem ipsum dolor sit amet, consectetuer adipiscing elit, sed diam nonummy</h3>
<p class="post-text" style="left:143px">olore magna aliquam erat volutpat. Ut wisi enim minim veniam, quis nostrud exerci tationcorper suscipit lobortis nisl ut aliquip ex ea</p>
<p class="post-text" style="left:455px">olore magna aliquam erat volutpat. Ut wisi enim minim veniam, quis nostrud exerci tationcorper suscipit lobortis nisl ut aliquip ex ea</p>
<p class="post-text" style="left:768px">olore magna aliquam erat volutpat. Ut wisi enim minim veniam, quis nostrud exerci tationcorper suscipit lobortis nisl ut aliquip ex ea</p>
<a class="btn btn-solid" style="left:143px;top:2918px;width:135px;height:32px;font-size:11.5px">Learn More <b style="width:22px;height:22px"><svg width="9" height="9" viewBox="0 0 10 10"><path d="M2 0l7 5-7 5z" fill="#65587b"/></svg></b></a>
<a class="btn btn-solid" style="left:455px;top:2918px;width:135px;height:32px;font-size:11.5px">Learn More <b style="width:22px;height:22px"><svg width="9" height="9" viewBox="0 0 10 10"><path d="M2 0l7 5-7 5z" fill="#65587b"/></svg></b></a>
<a class="btn btn-solid" style="left:768px;top:2918px;width:135px;height:32px;font-size:11.5px">Learn More <b style="width:22px;height:22px"><svg width="9" height="9" viewBox="0 0 10 10"><path d="M2 0l7 5-7 5z" fill="#65587b"/></svg></b></a>

<footer class="site-footer">
  <h2 class="footer-title heading" style="left:140px;top:68px">Quick Inquiry</h2>
  <div class="field" style="left:143px;top:132px;width:240px">First Name</div>
  <div class="field" style="left:398px;top:132px;width:240px">Last Name</div>
  <div class="field" style="left:143px;top:182px;width:240px">Phone</div>
  <div class="field" style="left:398px;top:182px;width:240px">Email</div>
  <div class="field" style="left:143px;top:232px;width:495px;height:78px">Message</div>
  <a class="btn btn-solid" style="left:143px;top:338px;width:132px;height:32px;font-size:11.5px">Submit Now <b style="width:22px;height:22px"><svg width="9" height="9" viewBox="0 0 10 10"><path d="M2 0l7 5-7 5z" fill="#65587b"/></svg></b></a>

  <h2 class="footer-title heading" style="left:766px;top:68px">Contact Us</h2>
  <div class="contact-row" style="top:132px"><i><svg width="12" height="16" viewBox="0 0 12 16"><path d="M6 0a6 6 0 0 1 6 6c0 4-6 10-6 10S0 10 0 6a6 6 0 0 1 6-6z" fill="#fff"/><circle cx="6" cy="6" r="2" fill="#65587b"/></svg></i><div><strong>Stone Trail Academy</strong><p>Lorem Street, Dolor sit amet<br>Mowrya Son, AB-123</p></div></div>
  <div class="contact-row" style="top:208px"><i><svg width="14" height="14" viewBox="0 0 14 14"><path d="M3 0l3 3-2 2c1 2 3 4 5 5l2-2 3 3-2 3C6 14 0 8 0 3z" fill="#fff"/></svg></i><div><strong>Phone</strong><p>123-456-7890</p></div></div>
  <div class="contact-row" style="top:268px"><i><svg width="14" height="10" viewBox="0 0 14 10"><rect width="14" height="10" fill="#fff"/><path d="M0 0l7 6 7-6" fill="none" stroke="#65587b"/></svg></i><div><strong>Email</strong><p>info@stonetrailacademy.com</p></div></div>
  <div class="follow"><span class="heading">Follow Us</span><i></i><i></i><i></i><i></i></div>
</footer>
<div class="copyright">Copyright © 2019 Stone Trail Academy. All Rights Reserved.</div>

</body>
</html>
```